Flyer for a marketing

We are a holistic mental health facility in need of a flyer to help promote our services and encourage more people to seek care. See the attachment to tell you more. We prefer warm green colors or rich blue. Thank you.

```html
<!DOCTYPE html>
<html lang="en">
<head>
<meta charset="utf-8">
<title>Evergreen Psychiatric Health and Wellness – Flyer</title>
<link rel="stylesheet" href="https://fonts.googleapis.com/css2?family=Montserrat:wght@400;500;600;700;800&display=swap">
<style>
  :root {
    --sky: #31c1ee;
    --navy: #1e3464;
    --paper: #f6f8f8;
    --white: #ffffff;
    --photo-a: #c9b79a;
    --photo-b: #5f7fb8;
  }
  * { margin: 0; padding: 0; box-sizing: border-box; }
  html, body { width: 927px; height: 1200px; overflow: hidden; background: var(--white); }
  body { font-family: "Montserrat", sans-serif; color: var(--navy); }
  .flyer { position: relative; width: 927px; height: 1200px; overflow: hidden; background: var(--white); }
  .abs { position: absolute; }

  .band-sky-top { left: 0; top: 0; width: 927px; height: 41px; background: var(--sky); }
  .band-navy { left: 0; width: 927px; height: 29px; background: var(--navy); }
  .band-navy.upper { top: 41px; }
  .band-navy.lower { top: 327px; }
  .header { left: 0; top: 70px; width: 927px; height: 257px; background: var(--paper); }

  .brand-dot { left: 88px; top: 118px; width: 120px; height: 120px; border-radius: 50%; background: var(--sky); }
  .brand-name { left: 250px; top: 88px; font-size: 27px; line-height: 33px; font-weight: 700; color: var(--navy); }
  .tagline { left: 0; width: 502px; top: 278px; text-align: center; font-size: 30px; font-weight: 400; letter-spacing: 1px; color: var(--navy); }

  .photo { left: 519px; top: 75px; width: 373px; height: 248px;
    background: linear-gradient(135deg, var(--photo-a) 0%, #e8d9c2 40%, var(--photo-b) 100%); }

  .mid-bg { left: 0; top: 356px; }

  .headline { left: 0; width: 927px; top: 380px; text-align: center; font-weight: 700; color: var(--navy); }
  .headline .line1 { font-size: 27px; line-height: 38px; }
  .headline .line2 { font-size: 26px; line-height: 38px; }

  .card { left: 89px; top: 482px; width: 749px; height: 520px; background: var(--white); }
  .card-head { left: 89px; top: 482px; width: 749px; height: 62px; background: var(--navy);
    color: var(--white); font-size: 30px; font-weight: 600; text-align: center; line-height: 62px; letter-spacing: -0.2px; }
  .invite { left: 89px; width: 749px; top: 556px; text-align: center; font-size: 26px; line-height: 31px; font-weight: 500; color: var(--navy); }

  .why { left: 225px; top: 646px; width: 469px; height: 75px; border-radius: 38px; background: var(--navy);
    color: var(--white); font-size: 46px; font-weight: 800; text-align: center; line-height: 75px; letter-spacing: -1px; }

  .reasons { left: 150px; top: 740px; width: 650px; list-style: none; }
  .reasons li { position: relative; padding-left: 38px; font-size: 21px; line-height: 32px; font-weight: 500; color: var(--navy); margin-bottom: 11px; }
  .reasons li::before { content: ""; position: absolute; left: 6px; top: 11px; width: 11px; height: 11px; border-radius: 50%; background: var(--navy); }

  .footer-bg { left: 0; top: 990px; }
  .contact { top: 1055px; font-size: 22px; line-height: 36.5px; font-weight: 600; color: var(--white); }
  .contact.left { right: 556px; text-align: right; }
  .contact.right { left: 410px; text-align: left; }
  .divider { left: 391px; top: 1048px; width: 2px; height: 122px; background: var(--white); }
</style>
</head>
<body>
<div class="flyer">
  <div class="abs band-sky-top"></div>
  <div class="abs band-navy upper"></div>
  <div class="abs header"></div>

  <div class="abs brand-dot"></div>
  <div class="abs brand-name">Evergreen<br>Psychiatric<br>Health<br>and<br>Wellness</div>
  <div class="abs tagline">The Care You Deserve</div>

  <div class="abs photo" role="img" aria-label="Photo of a smiling family: father, mother and young daughter embracing outdoors"></div>

  <div class="abs band-navy lower"></div>

  <svg class="abs mid-bg" width="927" height="430" viewBox="0 0 927 430" aria-hidden="true">
    <polygon points="0,0 927,0 927,386 838,422 89,422 0,386" fill="var(--sky)"/>
  </svg>

  <div class="abs headline">
    <div class="line1">Evergreen Psychiatric Health and Wellness</div>
    <div class="line2">where deserving patients meet compassionate providers</div>
  </div>

  <div class="abs card"></div>
  <div class="abs card-head">We are accepting new patients, no waiting list</div>
  <p class="abs invite">Your mental health matters, so make it a priority<br>and call us today for an appointment</p>

  <div class="abs why">Why choose us?</div>

  <ul class="abs reasons">
    <li>We are an integrative holistic psychiatric center.</li>
    <li>Our mission is to provide compassionate quality care.</li>
    <li>We provide psychiatric services including medication management and psychotherapy.</li>
    <li>We listen, care, and empower you to live better.</li>
    <li>We accept major insurances.</li>
  </ul>

  <svg class="abs footer-bg" width="927" height="210" viewBox="0 0 927 210" aria-hidden="true">
    <polygon points="0,41 463,9 927,41 927,210 0,210" fill="var(--sky)"/>
    <polygon points="0,58 468,27 927,58 927,210 0,210" fill="var(--navy)"/>
  </svg>

  <div class="abs contact left">Maple Grove, CA 90000<br>Fax (555) 014 - 2270<br>Ph (555) 018 - 4431</div>
  <div class="abs divider"></div>
  <div class="abs contact right">1450 Willow Creek Road, Suite 300<br>info@evergreenpsychhealth.com<br>evergreenpsychhealth.com</div>
</div>
</body>
</html>
```